energy rating company

Web Design graphics and layout only

To create two pages for the website. First the home page and the second is the design for the job board for our clients use after login. I have attached files that explain in detail what the pages should have and the purpose/desires of each object. Please read these thoroughly.

The webpages need to be clean, professional, easy on the eye, obvious in all its buttons and functions with a strong call to action on the home page and branding and clean, great and obvious looking buttons and very simple but dynamic as well. We wish to be seen as contemporary.

Business Concept

Our business concept is simple, to build a website whereby our clients will be able to upload jobs for energy raters to quote on and subsequent complete the work if their quote is selected. To link energy ratings that are required with energy raters via our website. Similarly to the varlo website, jobs will be “advertised” on the job board and raters will select which jobs they wish to quote for.

I have attached a Word document explaining all the parts of the website and another word document showing what we are sort of after and a excel spreadsheet as well. Please read these in conjunction with this brief!
Updates

Dear All

I have submitted with my brief a word doc and excel spreadsheet of the two pages I want created.  However this is not the layout or design I want, I only put it together so that you will need to know what is required on each page.  Feel free to change and redesign it all.

Also the second page does not require the "process" logo or any other menu items except the first five being Home, How it works, About Us, testimonials and Contact us as per the home page.

We also are looking for something very professional and very clean.  It should be very easy to see exactly what you are looking for.

I will also extend the deadline for new designers!!  I am excited to see your talents!!

Thanks

I have increase budget and posted a note saying feel free to change all the details layout etc on my brief just include everything!!! 

Wanting a professional corporate look...

Want a professional corporate look

We have changed our minds and you we no longer require the process to be on the home page.

Thanks

Target Market(s)

Target Market

Home Inspection Companies
Pest Inspection Companies
Residential home buyers/sellers
Real Estate companies

Industry/Entity Type

It Company

Number of Pages Required

1 page

Requirements
Must have
• Colours and Styles

• The website should be mainly white as I believe it is seen as clean and simple with colour from the logos, but can be swayed if it projects the image we are after.

• It should be obvious and process orientated and I do believe symbols, pictures, etc should replace words where possible.

```html
<!DOCTYPE html>
<html lang="en">
<head>
<meta charset="utf-8">
<title>ratewell australia – Home</title>
<link rel="stylesheet" href="https://fonts.googleapis.com/css2?family=Source+Sans+3:ital,wght@0,400;0,600;0,700;1,400&display=swap">
<style>
:root{
  --orange:#b5500f;
  --green-dark:#178a2c;
  --green-bright:#7cbf1c;
  --green-top:#5fae1a;
  --grey-band:#efefef;
  --text:#555;
  --text-soft:#777;
  --line:#d8d8d8;
  --white:#fff;
}
*{box-sizing:border-box;margin:0;padding:0}
html,body{width:1010px;height:1200px;overflow:hidden}
body{
  font-family:"Source Sans 3",sans-serif;color:var(--text);
  background:linear-gradient(#1f1f22 0%,#4a4a4d 20%,#9a9a9c 55%,#e4e4e6 85%,#fafafa 100%);
  position:relative;
}
.page{position:absolute;left:144px;top:152px;width:729px;height:889px;background:#f3f3f3}
.page-top{position:absolute;left:0;top:0;width:729px;height:120px;background:var(--white)}
.abs{position:absolute}
.brand{left:69px;top:34px;display:flex;align-items:center;gap:7px}
.brand-dot{width:38px;height:38px;border-radius:50%;background:var(--green-bright)}
.brand-name{color:var(--orange);font-weight:700;font-size:30px;line-height:1;letter-spacing:-.5px}
.account-links{left:597px;top:56px;font-size:8px;color:var(--green-dark)}
.account-links span{color:var(--orange)}
.card{left:21px;top:101px;width:686px;height:715px;background:var(--white);border-radius:8px;box-shadow:0 1px 4px rgba(0,0,0,.3);overflow:hidden}
.nav{position:absolute;top:17px;display:flex;font-size:10px;color:var(--text)}
.nav a{color:inherit;text-decoration:none;position:absolute;white-space:nowrap}
.nav a.current{font-weight:700}
.search{left:522px;top:13px;width:113px;height:18px;border-radius:9px;background:var(--white);box-shadow:0 1px 3px rgba(0,0,0,.35) inset,0 1px 2px rgba(0,0,0,.2)}
.band{left:0;top:50px;width:685px;height:154px;background:var(--grey-band)}
.tab{top:50px;width:94px;height:40px;border-radius:0 0 6px 6px;background:linear-gradient(var(--green-top),#a5d21b);color:var(--white);font-size:9.5px;line-height:1.3;text-align:center;display:flex;align-items:center;justify-content:center;box-shadow:0 2px 3px rgba(0,0,0,.25)}
.step{color:var(--green-dark);font-style:italic;font-size:13.5px;line-height:17px;text-align:center;transform:translate(-50%,-50%);white-space:nowrap}
.step-arrow{width:24px;height:28px;transform:translate(-50%,-50%)}
.intro{left:50px;top:231px;width:450px;font-size:10px;line-height:13px}
.intro .name{color:var(--orange);font-size:13.5px}
.headline{left:50px;top:268px;width:460px;color:var(--orange);font-size:16px;line-height:20px}
.cta{left:48px;top:342px;width:458px;height:38px;border-radius:7px;background:linear-gradient(var(--green-top),#a9d61b);color:var(--white);font-size:10px;display:flex;align-items:center;padding-left:14px;box-shadow:0 2px 3px rgba(0,0,0,.2)}
.cta b{font-weight:400;font-size:13px}
.register{left:50px;top:404px;width:460px;font-size:10px;line-height:13px}
.benefits{left:71px;top:440px;list-style:none;font-size:10px;font-style:italic;color:var(--green-dark)}
.benefits li{height:17.2px;display:flex;align-items:center;gap:5px}
.benefits svg{width:8px;height:8px;flex:none}
.closing{left:50px;top:625px;width:460px;font-size:10px;line-height:13px}
.closing em{font-style:normal;color:var(--orange);font-size:13px}
.panel{background:#eee;border-radius:7px}
.login{left:520px;top:219px;width:115px;height:115px}
.panel-title{position:absolute;left:6px;top:10px;color:var(--orange);font-size:13.5px}
.field-label{position:absolute;font-size:7px;color:var(--text-soft)}
.field{position:absolute;left:44px;width:64px;height:11px;border-radius:6px;background:var(--white);box-shadow:0 1px 2px rgba(0,0,0,.3) inset}
.login-btn{position:absolute;left:58px;top:79px;width:50px;height:11px;border-radius:6px;background:var(--orange);color:var(--white);font-size:7px;text-align:center;line-height:11px}
.testimonials{left:520px;top:343px;width:115px;height:319px}
.t-list{position:absolute;left:7px;top:30px;width:90px;list-style:none}
.t-list li{height:34px;display:flex;align-items:center;gap:5px;border-bottom:1px solid var(--line)}
.t-list svg{width:22px;height:22px;flex:none}
.t-name{font-size:9px;color:var(--green-dark);line-height:1}
.t-meta{font-size:4px;color:#999;line-height:1.4}
.scroll{position:absolute;left:102px;top:32px;width:2px;height:270px;background:#ddd}
.scroll::before{content:"";position:absolute;left:-3px;top:8px;width:8px;height:10px;border-radius:4px;background:#e4e4e4}
.footer-nav{top:837px}
.copyright{left:517px;top:839px;font-size:7.5px;font-style:italic;color:var(--text)}
</style>
</head>
<body>
<div class="page">
  <div class="page-top"></div>
  <div class="abs brand"><span class="brand-dot"></span><span class="brand-name">ratewell</span></div>
  <div class="abs account-links">Log in <span>Register</span></div>

  <div class="abs card">
    <nav class="nav">
      <a class="current" style="left:47px">Home</a>
      <a style="left:88px">How it works?</a>
      <a style="left:161px">About Us</a>
      <a style="left:215px">Testimonials</a>
      <a style="left:286px">Contact Us</a>
      <a style="left:349px">Help</a>
    </nav>
    <div class="abs search">
      <svg width="14" height="14" viewBox="0 0 14 14" style="position:absolute;left:5px;top:2px"><circle cx="6" cy="6" r="4" fill="none" stroke="#bbb" stroke-width="1.3"/><path d="M9 9l3 3" stroke="#bbb" stroke-width="1.5"/></svg>
    </div>

    <div class="abs band"></div>
    <div class="abs tab" style="left:330px">Get a quote</div>
    <div class="abs tab" style="left:437px">Energy Raters<br>Add your busines</div>
    <div class="abs tab" style="left:540px">Active<br>Job Board</div>

    <div class="abs step" style="left:83px;top:146px">Post a Job</div>
    <div class="abs step" style="left:212px;top:145px">Get As many<br>Quotes<br>as you like</div>
    <div class="abs step" style="left:341px;top:145px">Select<br>Energy<br>Quote<br>that suits</div>
    <div class="abs step" style="left:472px;top:146px">Approve<br>Payment</div>
    <div class="abs step" style="left:597px;top:146px">Receive<br>Rating</div>
    <svg class="abs step-arrow" style="left:150px;top:146px" viewBox="0 0 24 28"><path d="M4 2c-4 8 0 14 8 15v-5l10 10-10 6v-5C3 22-2 12 4 2z" fill="var(--green-dark)"/></svg>
    <svg class="abs step-arrow" style="left:279px;top:146px" viewBox="0 0 24 28"><path d="M4 2c-4 8 0 14 8 15v-5l10 10-10 6v-5C3 22-2 12 4 2z" fill="var(--green-dark)"/></svg>
    <svg class="abs step-arrow" style="left:406px;top:146px" viewBox="0 0 24 28"><path d="M4 2c-4 8 0 14 8 15v-5l10 10-10 6v-5C3 22-2 12 4 2z" fill="var(--green-dark)"/></svg>
    <svg class="abs step-arrow" style="left:535px;top:146px" viewBox="0 0 24 28"><path d="M4 2c-4 8 0 14 8 15v-5l10 10-10 6v-5C3 22-2 12 4 2z" fill="var(--green-dark)"/></svg>

    <p class="abs intro"><span class="name">ratewell australia</span> is Australia’s leading professional energy rating consultancy firm specializing in large scaled residential and commercial energy rating logistics.</p>
    <h1 class="abs headline" style="font-weight:400">We have professional and accredited energy raters in all States and Territories ready and waiting to provide quotes for and perform &nbsp;your energy rating jobs!</h1>
    <div class="abs cta">It’s&nbsp;<b>Free</b>,&nbsp;<b>Fast</b>&nbsp;and&nbsp;<b>Easy</b>&nbsp;to use and you get the best price and turnaround time that suits you!!</div>
    <p class="abs register">Register with us, upload your job and specifications, and sit back and watch as energy raters provide quotes for your work!</p>
    <ul class="abs benefits">
      <li><svg viewBox="0 0 8 8"><path d="M0.5 4.3l2.2 2.4L7.5 1" fill="none" stroke="var(--green-dark)" stroke-width="1.6"/></svg>Get the best priced quotes for your energy ratings</li>
      <li><svg viewBox="0 0 8 8"><path d="M0.5 4.3l2.2 2.4L7.5 1" fill="none" stroke="var(--green-dark)" stroke-width="1.6"/></svg>Save time by listing a job to get many quotes</li>
      <li><svg viewBox="0 0 8 8"><path d="M0.5 4.3l2.2 2.4L7.5 1" fill="none" stroke="var(--green-dark)" stroke-width="1.6"/></svg>Monitor your jobs and quotes on your own job board</li>
      <li><svg viewBox="0 0 8 8"><path d="M0.5 4.3l2.2 2.4L7.5 1" fill="none" stroke="var(--green-dark)" stroke-width="1.6"/></svg>Be notified via email of all new quotes as they come in</li>
      <li><svg viewBox="0 0 8 8"><path d="M0.5 4.3l2.2 2.4L7.5 1" fill="none" stroke="var(--green-dark)" stroke-width="1.6"/></svg>Be able to specify your dturnaround times</li>
      <li><svg viewBox="0 0 8 8"><path d="M0.5 4.3l2.2 2.4L7.5 1" fill="none" stroke="var(--green-dark)" stroke-width="1.6"/></svg>Accessible anytime and anywhere</li>
      <li><svg viewBox="0 0 8 8"><path d="M0.5 4.3l2.2 2.4L7.5 1" fill="none" stroke="var(--green-dark)" stroke-width="1.6"/></svg>Choose a deadline for energy raters to supply quotes</li>
      <li><svg viewBox="0 0 8 8"><path d="M0.5 4.3l2.2 2.4L7.5 1" fill="none" stroke="var(--green-dark)" stroke-width="1.6"/></svg>Have access to many qualified energy raters in your state all quoting for your work</li>
      <li><svg viewBox="0 0 8 8"><path d="M0.5 4.3l2.2 2.4L7.5 1" fill="none" stroke="var(--green-dark)" stroke-width="1.6"/></svg>Be able to track your jobs and pay online</li>
      <li><svg viewBox="0 0 8 8"><path d="M0.5 4.3l2.2 2.4L7.5 1" fill="none" stroke="var(--green-dark)" stroke-width="1.6"/></svg>Provide feedback on energy raters</li>
    </ul>
    <p class="abs closing">Its <em>totally free to be registered</em> with us and there is no obligations or hidden catches! &nbsp;So if you wish to utilise the amazing opportunity register now! &nbsp;This new website will be going live on the (insert date) so be ready to <em>save some money!</em></p>

    <div class="abs panel login">
      <div class="panel-title">Login area</div>
      <span class="field-label" style="left:27px;top:42px">Email</span>
      <span class="field" style="top:40px"></span>
      <span class="field-label" style="left:8px;top:61px">Password</span>
      <span class="field" style="top:59px"></span>
      <span class="login-btn">Login</span>
    </div>

    <div class="abs panel testimonials">
      <div class="panel-title">Testimonials</div>
      <ul class="t-list">
        <li><svg viewBox="0 0 22 22"><rect x=".5" y=".5" width="21" height="21" fill="#fff" stroke="#555"/><path d="M.5 .5L21.5 21.5M21.5 .5L.5 21.5" stroke="#555"/></svg><div><div class="t-name">Testimonial 1</div><div class="t-meta">25.03.2010 | 12 comments</div></div></li>
        <li><svg viewBox="0 0 22 22"><rect x=".5" y=".5" width="21" height="21" fill="#fff" stroke="#555"/><path d="M.5 .5L21.5 21.5M21.5 .5L.5 21.5" stroke="#555"/></svg><div><div class="t-name">Testimonial 2</div><div class="t-meta">25.03.2010 | 12 comments</div></div></li>
        <li><svg viewBox="0 0 22 22"><rect x=".5" y=".5" width="21" height="21" fill="#fff" stroke="#555"/><path d="M.5 .5L21.5 21.5M21.5 .5L.5 21.5" stroke="#555"/></svg><div><div class="t-name">Testimonial 3</div><div class="t-meta">25.03.2010 | 12 comments</div></div></li>
        <li><svg viewBox="0 0 22 22"><rect x=".5" y=".5" width="21" height="21" fill="#fff" stroke="#555"/><path d="M.5 .5L21.5 21.5M21.5 .5L.5 21.5" stroke="#555"/></svg><div><div class="t-name">Testimonial 4</div><div class="t-meta">25.03.2010 | 12 comments</div></div></li>
        <li><svg viewBox="0 0 22 22"><rect x=".5" y=".5" width="21" height="21" fill="#fff" stroke="#555"/><path d="M.5 .5L21.5 21.5M21.5 .5L.5 21.5" stroke="#555"/></svg><div><div class="t-name">Testimonial 5</div><div class="t-meta">25.03.2010 | 12 comments</div></div></li>
        <li><svg viewBox="0 0 22 22"><rect x=".5" y=".5" width="21" height="21" fill="#fff" stroke="#555"/><path d="M.5 .5L21.5 21.5M21.5 .5L.5 21.5" stroke="#555"/></svg><div><div class="t-name">Testimonial 6</div><div class="t-meta">25.03.2010 | 12 comments</div></div></li>
        <li><svg viewBox="0 0 22 22"><rect x=".5" y=".5" width="21" height="21" fill="#fff" stroke="#555"/><path d="M.5 .5L21.5 21.5M21.5 .5L.5 21.5" stroke="#555"/></svg><div><div class="t-name">Testimonial 7</div><div class="t-meta">25.03.2010 | 12 comments</div></div></li>
        <li style="border-bottom:none"><svg viewBox="0 0 22 22"><rect x=".5" y=".5" width="21" height="21" fill="#fff" stroke="#555"/><path d="M.5 .5L21.5 21.5M21.5 .5L.5 21.5" stroke="#555"/></svg><div><div class="t-name">Testimonial 7</div><div class="t-meta">25.03.2010 | 12 comments</div></div></li>
      </ul>
      <div class="scroll"></div>
    </div>
  </div>

  <nav class="nav footer-nav">
    <a class="current" style="left:68px">Home</a>
    <a style="left:109px">How it works?</a>
    <a style="left:182px">About Us</a>
    <a style="left:236px">Testimonials</a>
    <a style="left:307px">Contact Us</a>
    <a style="left:370px">Help</a>
  </nav>
  <div class="abs copyright">Copyright © 2010 ratewell australia. All rights reserved.</div>
</div>
</body>
</html>
```